Harborline Crest Insurance Services

we are a high end insurance agency we specialize on Auto | Home | Business | Life looking for something professional and luxuries at the same time. if you guys need anything else please let me know.

Auto | Home | Business | Life must be under logo on the back with black background.

i want the back part to be black with our gold logo on it.

Target Market(s)

Auto | Home | Business | Life

Industry/Entity Type

Insurance Broker

Contact Information for Business Card

My logo is gold so a black in the back would be nice.

Font styles to use
Serif

Colors
000000

Requirements
Must have
• Big logo on the back with black background.

```html
<!DOCTYPE html>
<html lang="en">
<head>
<meta charset="utf-8">
<title>Harborline Crest Insurance Services – Business Card</title>
<link href="https://fonts.googleapis.com/css2?family=Arimo:wght@400;700&display=swap" rel="stylesheet">
<style>
  :root {
    --stage: #1f1f1f;
    --card-black: #050505;
    --gold: #e8b828;
    --gold-deep: #c99a1a;
    --silver: #9a9a9a;
    --ghost: #3a3a3a;
    --white: #f2f2f2;
  }
  * { margin: 0; padding: 0; box-sizing: border-box; }
  html, body {
    width: 1200px; height: 997px; overflow: hidden;
    background: var(--stage);
    font-family: "Arimo", Arial, sans-serif;
  }
  .card {
    position: absolute;
    width: 540px; height: 309px;
    background: var(--card-black);
    box-shadow: 0 12px 30px rgba(0,0,0,.6);
    overflow: hidden;
  }

  /* Back of card */
  .card-back { left: 30px; top: 344px; }
  .back-brand {
    position: absolute; left: 0; right: 0; top: 62px;
    display: flex; flex-direction: column; align-items: center;
  }
  .brand-dot {
    width: 58px; height: 58px; border-radius: 50%;
    background: var(--gold); margin-bottom: 16px;
  }
  .brand-name {
    color: var(--gold); font-weight: 700; text-align: center;
    font-size: 26px; line-height: 1.15; letter-spacing: .5px;
  }
  .service-lines {
    margin-top: 16px; font-size: 13px; letter-spacing: 2px;
    color: var(--gold);
  }
  .service-lines .divider { color: var(--silver); margin: 0 4px; }

  /* Front of card */
  .card-front { left: 630px; top: 344px; }
  .front-brand {
    position: absolute; left: 40px; top: 30px;
    display: flex; align-items: center; gap: 16px;
  }
  .front-brand .brand-dot { width: 48px; height: 48px; margin: 0; }
  .front-brand .brand-name { font-size: 20px; text-align: left; }
  .name-band {
    position: absolute; left: 0; right: 0; top: 108px; height: 38px;
    background: linear-gradient(var(--gold), var(--gold-deep));
    text-align: center; color: #111;
  }
  .person-name { font-weight: 700; font-size: 14px; letter-spacing: .5px; padding-top: 4px; }
  .person-role { font-size: 11px; letter-spacing: 1px; }
  .ghost-mark {
    position: absolute; right: 50px; top: 30px;
    width: 60px; height: 60px; border-radius: 50%; background: var(--ghost);
  }
  .contact-list {
    position: absolute; left: 40px; top: 162px;
    list-style: none; color: var(--white); font-size: 13px; line-height: 18px;
  }
  .contact-list li { display: flex; align-items: center; gap: 8px; }
  .contact-list svg { width: 11px; height: 11px; fill: var(--gold); }
  .address { margin-top: 4px; font-weight: 700; padding-left: 19px; }
  .web-band {
    position: absolute; left: 0; right: 0; top: 258px; height: 22px;
    background: linear-gradient(var(--gold), var(--gold-deep));
    text-align: right; padding-right: 40px;
    color: #111; font-weight: 700; font-size: 11px; letter-spacing: 3px; line-height: 22px;
  }
  .base-strip {
    position: absolute; left: 0; right: 0; bottom: 0; height: 8px;
    background: var(--gold-deep);
  }
</style>
</head>
<body>

<section class="card card-back">
  <div class="back-brand">
    <span class="brand-dot"></span>
    <p class="brand-name">Harborline Crest<br>Insurance Services</p>
    <p class="service-lines">AUTO<span class="divider">|</span>HOME<span class="divider">|</span>BUSINESS<span class="divider">|</span>LIFE</p>
  </div>
</section>

<section class="card card-front">
  <div class="front-brand">
    <span class="brand-dot"></span>
    <p class="brand-name">Harborline Crest<br>Insurance Services</p>
  </div>
  <span class="ghost-mark"></span>
  <div class="name-band">
    <p class="person-name">MARCUS ELLORY</p>
    <p class="person-role">DIRECTOR</p>
  </div>
  <ul class="contact-list">
    <li><svg viewBox="0 0 12 12"><path d="M1 3c0-1 1-2 2-2h6c1 0 2 1 2 2v1H8V3H4v1H1zM2 5h8l1 6H1z"/></svg>+61 3 9000 4120</li>
    <li><svg viewBox="0 0 12 12"><rect x="3" y="0" width="6" height="12" rx="1.2"/></svg>+61 400 555 218</li>
    <li><svg viewBox="0 0 12 12"><path d="M0 2h12v8H0zM1 3l5 4 5-4" stroke="#050505" stroke-width="1"/></svg>marcus@hcis.com</li>
    <li class="address">Level 5, 42 Harbour Lane<br>Melbourne VIC 3000 Australia</li>
  </ul>
  <div class="web-band">www.hcis.com</div>
  <div class="base-strip"></div>
</section>

</body>
</html>
```